Law Firm in Texas in need of new letterhead

Law Firm in Fort Worth, TX, USA named "Vale & Brennick, Attorneys-At-Law, LLP." This is a general practice law firm that mostly does Family Law and Criminal Defense work.

We are looking for a new letterhead that has a "classical" appeal, with modern elements.

Any color combination is fine, but please note that we do fax many documents, so the design must be clearly legible in Black and White.

We would like our letterhead to project a sense of professionalism, integrity, and ability.

Target Market(s)

Letterhead will be for correspondence generally with other attorneys and clients.

Industry/Entity Type

Law Firm

Logo Text

Vale & Brennick, Attorneys-At-Law, LLP.

Logo styles of interest
Pictorial/Combination Logo
Wordmark Logo
Lettermark Logo
Requirements
Nice to have
• Although not necessary, a "Texas Star" that is incorporated into the design would be a nice touch.
Should not have
• Colors that do not convert to B&W easily

```html
<!DOCTYPE html>
<html lang="en">
<head>
<meta charset="utf-8">
<title>Vale &amp; Brennick — Letterhead</title>
<link rel="stylesheet" href="https://fonts.googleapis.com/css2?family=Arimo&family=Roboto+Slab:wght@300&display=swap">
<style>
  :root {
    --paper: #ffffff;
    --ink: #111111;
    --emblem-grey: #c9c9c9;
  }
  html, body {
    margin: 0;
    padding: 0;
    overflow: hidden;
    background: var(--paper);
  }
  .letterhead {
    position: relative;
    width: 927px;
    height: 1200px;
    overflow: hidden;
    background: var(--paper);
  }
  .emblem {
    position: absolute;
    inset: 0;
    width: 927px;
    height: 1200px;
  }
  .masthead {
    position: absolute;
    top: 0;
    left: 0;
    width: 927px;
  }
  .firm-name {
    margin: 0;
    padding-top: 18px;
    text-align: center;
    font-family: "Roboto Slab", serif;
    font-weight: 300;
    font-size: 33px;
    line-height: 42px;
    color: var(--ink);
  }
  .masthead-rule {
    margin: 5px 0 0 56px;
    width: 834px;
    height: 4px;
    background: var(--ink);
  }
  .contact-line {
    margin: 3px 0 0 104px;
    display: flex;
    gap: 0;
    font-family: "Arimo", sans-serif;
    font-size: 15.5px;
    line-height: 20px;
    color: var(--ink);
  }
  .contact-address { width: 390px; }
  .contact-phone { width: 167px; }
</style>
</head>
<body>
  <div class="letterhead">
    <svg class="emblem" viewBox="0 0 927 1200" aria-hidden="false">
      <circle cx="155" cy="664" r="560" fill="none" stroke="var(--emblem-grey)" stroke-width="190"/>
      <circle cx="155" cy="664" r="465" fill="var(--emblem-grey)" opacity="0.55"
              role="img" aria-label="Large faint Texas star set inside the ring"/>
    </svg>

    <header class="masthead">
      <h1 class="firm-name">Vale &amp; Brennick, Attorneys-At-Law, LLP</h1>
      <div class="masthead-rule"></div>
      <p class="contact-line">
        <span class="contact-address">1842 W. Magnolia Ave. Fort Worth, TX 76104</span>
        <span class="contact-phone">(817) 555-0142</span>
        <span class="contact-fax">(817) 555-0187 (fax)</span>
      </p>
    </header>
  </div>
</body>
</html>
```